Maple Ridge business card design

Card needs to include the following text/items:
Company Logo
Tobin Marsh
Phone # - 555-318-7642
service@mapleridgelandscaping.example
Lawn & landscape maintenance services

```html
<!DOCTYPE html>
<html lang="en">
<head>
<meta charset="utf-8">
<title>Maple Ridge Business Card</title>
<link href="https://fonts.googleapis.com/css2?family=Cinzel:wght@500;600&family=Tinos&display=swap" rel="stylesheet">
<style>
  :root {
    --page-bg: #e6e6e6;
    --card-white: #ffffff;
    --forest: #0f5a2f;
    --forest-deep: #0a4527;
    --forest-light: #076847;
    --leaf: #7fa33a;
    --amber: #f2a000;
    --bark: #9a6a22;
    --mist: #eef2ea;
    --ink-grey: #555a55;
    --on-dark: #ffffff;
  }
  * { margin: 0; padding: 0; box-sizing: border-box; }
  html, body {
    width: 1200px; height: 1200px; overflow: hidden;
    background: var(--page-bg);
  }
  .canvas { position: relative; width: 1200px; height: 1200px; }
  .card {
    position: absolute; left: 257px; width: 686px; height: 391px;
    border-radius: 17px; overflow: hidden;
  }
  .card--front { top: 159px; background: var(--card-white); }
  .card--back {
    top: 650px;
    background: linear-gradient(135deg, var(--forest-deep) 0%, var(--forest) 45%, var(--forest-light) 100%);
  }
  .card-art { position: absolute; inset: 0; width: 100%; height: 100%; }

  .contact { position: absolute; left: 54px; top: 128px; }
  .contact__name {
    font-family: "Cinzel", serif; font-weight: 600; font-size: 30px;
    color: var(--forest); letter-spacing: 0.5px; line-height: 1;
  }
  .contact__row {
    display: flex; align-items: center; gap: 9px;
    font-family: "Tinos", serif; color: var(--ink-grey);
  }
  .contact__row svg { flex: none; }
  .contact__row--phone { margin-top: 12px; font-size: 28px; line-height: 1; }
  .contact__row--small { font-size: 14px; margin-top: 4px; }
  .contact__row--phone + .contact__row--small { margin-top: 8px; }

  .brand {
    position: absolute; left: 400px; top: 56px; width: 210px;
    display: flex; flex-direction: column; align-items: center;
  }
  .brand__dot { width: 118px; height: 118px; border-radius: 50%; background: var(--leaf); }
  .brand__name {
    margin-top: 20px;
    font-family: "Cinzel", serif; font-weight: 600; font-size: 32px;
    color: var(--forest); white-space: nowrap; line-height: 1;
  }

  .tagline {
    font-family: "Cinzel", serif; font-weight: 500; color: var(--on-dark);
    text-align: center; font-size: 16px; letter-spacing: 0.4px; line-height: 1.25;
  }
  .tagline--front { position: absolute; left: 58px; width: 250px; top: 325px; }
  .tagline--back { position: absolute; left: 0; right: 0; top: 330px; }

  .brand--back { left: 0; right: 0; width: auto; top: 60px; }
  .brand--back .brand__dot { width: 150px; height: 150px; background: var(--mist); }
  .brand--back .brand__name { color: var(--on-dark); font-size: 38px; margin-top: 26px; }
</style>
</head>
<body>
<div class="canvas">

  <section class="card card--front">
    <svg class="card-art" viewBox="0 0 686 391" aria-hidden="true">
      <circle cx="149" cy="177" r="154" fill="var(--mist)"/>
      <path d="M0 327 C 90 300, 150 282, 220 282 C 330 282, 420 340, 510 336 C 580 333, 640 300, 686 282 L686 391 L0 391 Z" fill="var(--bark)"/>
      <path d="M0 330 C 90 305, 150 290, 220 290 C 330 290, 420 345, 510 342 C 580 339, 640 306, 686 288 L686 391 L0 391 Z" fill="var(--amber)"/>
      <path d="M0 340 C 90 315, 150 300, 220 300 C 330 300, 420 352, 510 349 C 580 346, 640 314, 686 296 L686 391 L0 391 Z" fill="var(--leaf)"/>
      <path d="M0 348 C 90 325, 150 312, 220 312 C 330 312, 420 362, 510 360 C 580 358, 640 326, 686 310 L686 391 L0 391 Z" fill="var(--forest)"/>
    </svg>

    <div class="contact">
      <h1 class="contact__name">Tobin Marsh</h1>
      <p class="contact__row contact__row--phone">
        <svg width="14" height="14" viewBox="0 0 24 24"><path fill="var(--forest)" d="M6.6 10.8a15.1 15.1 0 0 0 6.6 6.6l2.2-2.2c.3-.3.7-.4 1-.2 1.1.4 2.3.6 3.6.6.6 0 1 .4 1 1V20c0 .6-.4 1-1 1A17 17 0 0 1 3 4c0-.6.4-1 1-1h3.5c.6 0 1 .4 1 1 0 1.3.2 2.5.6 3.6.1.3 0 .7-.2 1z"/></svg>
        555-318-7642
      </p>
      <p class="contact__row contact__row--small">
        <svg width="14" height="10" viewBox="0 0 14 10"><rect width="14" height="10" fill="var(--forest)"/><path d="M0 0 L7 6 L14 0" stroke="#fff" stroke-width="1.2" fill="none"/></svg>
        service@mapleridgelandscaping.example
      </p>
      <p class="contact__row contact__row--small">
        <svg width="14" height="14" viewBox="0 0 14 14"><circle cx="7" cy="7" r="7" fill="var(--forest)"/><path d="M1 7h12M7 1c-3 3-3 9 0 12M7 1c3 3 3 9 0 12" stroke="#fff" stroke-width="1" fill="none"/></svg>
        mapleridgelandscaping.example
      </p>
    </div>

    <div class="brand">
      <span class="brand__dot"></span>
      <span class="brand__name">Maple Ridge</span>
    </div>

    <p class="tagline tagline--front">Lawn &amp; Landscape<br>Maintenance Services</p>
  </section>

  <section class="card card--back">
    <div class="brand brand--back">
      <span class="brand__dot"></span>
      <span class="brand__name">Maple Ridge</span>
    </div>
    <p class="tagline tagline--back">Lawn &amp; Landscape Maintenance Services</p>
  </section>

</div>
</body>
</html>
```